Wine Label for White and Red Wine from California

We need a wine label for 2 whites and 2 red wines. (Merlot, Cabernet Sauvignon, Chardonnay, Pinot Grigio) Can be the same label or can have something to differentiate among them such as a color change. This is a label for an already existing wine on the US market but needs to be completely re-done. We want something way sharper, eye catching. Don't use the original label please as your starting point-- I don't think we want to see it anymore. But the structure of it is ok and the fonts are ok. (The tree is what is so awful about)

Target Market(s)

US market, always good to think of millennials, but still appeal to all ages. Men and women.

Colors

Designer to choose colors to be used in the design.

Requirements
Must have
• Should be eye catching, grabs attention, looks expensive, sells for a value price. Should feature the brand name and varietal and vintage:
• Korvel Vineyards / Cabernet Sauvignon / 2014
• Bottle type is the 'Bordeaux Style' bottle. The white wine is a green bottle, the red wine uses a dark brown bottle. Be sure the labels look good on these bottles.
• What this bottle looks like is shown below.
• The label we are replacing is shown in the briefs.
Nice to have
• We feel successful labels have a lot of white background, stay away from dark labels-- they scratch too much when handled.
• Attached is a label we like, please look at the Lumbra label image below. But at the same time, we are flexible to your creativity. But nothing too crazy please.
Should not have
• Should not have a dark background.
• We are not big fans of grapes on the label unless extremely stylised. Nor do we like wine glasses, wine bottles.

```html
<!DOCTYPE html>
<html lang="en">
<head>
<meta charset="utf-8">
<title>Korvel Vineyard – Cabernet Sauvignon 2014 Label</title>
<link rel="stylesheet" href="https://fonts.googleapis.com/css2?family=Federant&family=Marcellus&display=swap">
<style>
  :root {
    --canvas-bg: #ffffff;
    --label-paper: #f1f1f1;
    --pattern-tint: #ebe6da;
    --ink: #111111;
    --gold-dark: #d39b16;
    --gold-light: #f2c944;
    --gold-soft: #c9a24a;
  }
  * { margin: 0; padding: 0; box-sizing: border-box; }
  html, body {
    width: 1000px;
    height: 1200px;
    overflow: hidden;
    background: var(--canvas-bg);
  }
  .canvas {
    position: relative;
    width: 1000px;
    height: 1200px;
  }
  .wine-label {
    position: absolute;
    left: 115px;
    top: 159px;
    width: 770px;
    height: 882px;
    background: var(--label-paper);
    box-shadow: 2px 3px 6px rgba(0, 0, 0, 0.25);
    overflow: hidden;
    color: var(--ink);
    text-align: center;
  }
  .label-pattern {
    position: absolute;
    inset: 0;
    background: radial-gradient(circle at 50% 40%, var(--label-paper) 0%, var(--pattern-tint) 100%);
  }
  .label-emblem {
    position: absolute;
    left: 137px;
    top: 101px;
    width: 496px;
    height: 154px;
    background: linear-gradient(90deg, #3a3226 0%, #d9a928 30%, #efe9dc 50%, #d9a928 70%, #3a3226 100%);
    opacity: 0.55;
  }
  .brand-name {
    position: absolute;
    left: 0;
    right: 0;
    top: 328px;
    font-family: "Federant", serif;
    font-weight: 400;
    font-size: 100px;
    line-height: 112px;
    color: var(--ink);
  }
  .brand-name span { display: block; }
  .divider {
    position: absolute;
    left: 169px;
    top: 586px;
    width: 432px;
    height: 14px;
  }
  .details {
    position: absolute;
    left: 0;
    right: 0;
    top: 624px;
    font-family: "Marcellus", serif;
    font-size: 26px;
    line-height: 31px;
    letter-spacing: 0.5px;
    font-weight: 700;
  }
  .varietal {
    position: absolute;
    left: 0;
    right: 0;
    top: 738px;
    font-family: "Marcellus", serif;
    font-size: 36px;
    letter-spacing: 1px;
    font-weight: 700;
  }
  .vintage-band {
    position: absolute;
    left: 0;
    right: 0;
    bottom: 0;
    height: 77px;
    background: linear-gradient(90deg, var(--gold-dark) 0%, var(--gold-light) 50%, var(--gold-dark) 100%);
    display: flex;
    align-items: center;
    justify-content: center;
    font-family: "Marcellus", serif;
    font-size: 36px;
    font-weight: 700;
  }
</style>
</head>
<body>
<main class="canvas">
  <section class="wine-label">
    <div class="label-pattern" role="img" aria-label="Faint gold interlocking circle pattern across the white label"></div>
    <div class="label-emblem" role="img" aria-label="Stylised emblem illustration in black and gold"></div>

    <h1 class="brand-name">
      <span>Korvel</span>
      <span>Vineyard</span>
    </h1>

    <svg class="divider" viewBox="0 0 432 14" aria-hidden="true">
      <line x1="0" y1="7" x2="202" y2="7" stroke="#111" stroke-width="2.5"/>
      <line x1="230" y1="7" x2="432" y2="7" stroke="#111" stroke-width="2.5"/>
      <circle cx="216" cy="7" r="6" fill="#111"/>
    </svg>

    <p class="details">QUALITY WINES SINCE 1996<br>15% - 75ML</p>

    <p class="varietal">CABERNET SAUVIGNON</p>

    <div class="vintage-band">2014</div>
  </section>
</main>
</body>
</html>
```